Turn this into a clear and concise

Attached is a screen shot that we currently show to investors from a software program. We need you to illustrate this in a much more professional looking and easy to view and understand way. If we like your style and attention to detail there is more work behind this.
Industry/Entity Type
Software

```html
<!DOCTYPE html>
<html lang="en">
<head>
<meta charset="utf-8">
<title>Intra-day Countertrend US Hours – Example Trade</title>
<link rel="stylesheet" href="https://fonts.googleapis.com/css2?family=Josefin+Sans:wght@300;400;600&display=swap">
<style>
  :root{
    --paper:#ffffff;
    --ink:#111111;
    --accent:#e8741c;
    --panel:#cc5400;
    --grid:#f2a56c;
    --gridline:#f6dcc6;
    --label:#f7e2d0;
    --axis:#1a0a00;
    --up:#1f9a3a;
    --down:#e01414;
    --signal:#f2d21c;
    --rsi-glow:#ffffff;
    --rsi-core:#7fd8cc;
    --volume:#2b2be6;
    --timebar:#111111;
  }
  html,body{margin:0;padding:0;background:var(--paper);overflow:hidden;}
  .sheet{position:relative;width:1200px;height:927px;overflow:hidden;background:var(--paper);
    font-family:"Josefin Sans",sans-serif;color:var(--ink);}
  .sources{position:absolute;left:68px;top:38px;margin:0;}
  .sources__label{display:block;font-size:24px;font-weight:400;letter-spacing:1px;line-height:28px;}
  .sources__strategy{display:block;font-size:20px;font-weight:300;line-height:24px;}
  .sources__trade{display:block;font-size:20px;font-weight:300;line-height:24px;color:var(--accent);}
  .side-title{position:absolute;top:158px;margin:0;font-size:29px;font-weight:300;letter-spacing:1.5px;
    text-align:center;width:300px;}
  .side-title--entry{left:168px;}
  .side-title--exit{left:731px;}
  .charts{position:absolute;left:0;top:0;}
  .panel-title{font-family:"Josefin Sans",sans-serif;font-size:16px;fill:var(--label);text-anchor:middle;}
  .axis-label{font-family:"Josefin Sans",sans-serif;font-size:12px;fill:var(--label);}
  .axis-label--key{fill:var(--axis);font-weight:600;}
  .time-label{font-family:"Josefin Sans",sans-serif;font-size:13px;font-weight:600;fill:var(--accent);text-anchor:middle;}
  .wick{stroke:#2a1200;stroke-width:1;}
  .candle-up{fill:var(--up);stroke:#0d3d17;stroke-width:.6;}
  .candle-down{fill:var(--down);stroke:#5a0000;stroke-width:.6;}
  .doji{stroke:#2a1200;stroke-width:1.2;}
  .vol-bar{fill:var(--volume);}
</style>
</head>
<body>
<div class="sheet">
  <h1 class="sources">
    <span class="sources__label">SOURCES:</span>
    <span class="sources__strategy">Intra-day Countertrend US Hours</span>
    <span class="sources__trade">Example Trade: 30 year Treasury Bond, 7/31/14 “Payroll Friday”</span>
  </h1>
  <h2 class="side-title side-title--entry">ENTRY (SELL)</h2>
  <h2 class="side-title side-title--exit">EXIT (BUY)</h2>

  <svg class="charts" width="1200" height="927" viewBox="0 0 1200 927" xmlns="http://www.w3.org/2000/svg">
    <defs>
      <!-- shared chart frame: panels, grid, axis -->
      <g id="frame">
        <rect x="70" y="226" width="495" height="306" fill="var(--panel)"/>
        <rect x="70" y="546" width="495" height="160" fill="var(--panel)"/>
        <rect x="70" y="722" width="495" height="125" fill="var(--panel)"/>
        <g stroke="var(--grid)" stroke-width="1">
          <line x1="70" y1="297" x2="458" y2="297"/><line x1="70" y1="340" x2="458" y2="340"/>
          <line x1="70" y1="384" x2="458" y2="384"/><line x1="70" y1="427" x2="458" y2="427"/>
          <line x1="70" y1="470" x2="458" y2="470"/><line x1="70" y1="514" x2="458" y2="514"/>
          <line x1="70" y1="598" x2="458" y2="598"/><line x1="70" y1="645" x2="458" y2="645"/>
          <line x1="70" y1="690" x2="458" y2="690"/>
          <line x1="70" y1="773" x2="458" y2="773"/><line x1="70" y1="806" x2="458" y2="806"/>
        </g>
        <g stroke="var(--gridline)" stroke-width="1" opacity=".75">
          <line x1="118" y1="226" x2="118" y2="532"/><line x1="217" y1="226" x2="217" y2="532"/>
          <line x1="317" y1="226" x2="317" y2="532"/><line x1="416" y1="226" x2="416" y2="532"/>
          <line x1="118" y1="546" x2="118" y2="706"/><line x1="217" y1="546" x2="217" y2="706"/>
          <line x1="317" y1="546" x2="317" y2="706"/><line x1="416" y1="546" x2="416" y2="706"/>
          <line x1="118" y1="722" x2="118" y2="847"/><line x1="217" y1="722" x2="217" y2="847"/>
          <line x1="317" y1="722" x2="317" y2="847"/><line x1="416" y1="722" x2="416" y2="847"/>
        </g>
        <g stroke="var(--signal)" stroke-width="1">
          <line x1="70" y1="616" x2="565" y2="616"/><line x1="70" y1="673" x2="565" y2="673"/>
        </g>
        <g stroke="var(--axis)" stroke-width="1.2">
          <line x1="458" y1="258" x2="458" y2="532"/>
          <line x1="458" y1="590" x2="458" y2="706"/>
          <line x1="458" y1="760" x2="458" y2="847"/>
        </g>
        <text class="panel-title" x="317" y="245">Price</text>
        <text class="panel-title" x="317" y="567">'Relative Strength Index - RSI'</text>
        <text class="panel-title" x="317" y="742">Volume</text>
        <text class="axis-label" x="470" y="301">137.25</text>
        <text class="axis-label axis-label--key" x="470" y="345">137.00</text>
        <text class="axis-label" x="470" y="388">136.75</text>
        <text class="axis-label" x="470" y="431">136.50</text>
        <text class="axis-label" x="470" y="474">136.25</text>
        <text class="axis-label axis-label--key" x="470" y="518">136.00</text>
        <text class="axis-label" x="470" y="602">100</text>
        <text class="axis-label" x="470" y="620">80</text>
        <text class="axis-label" x="470" y="649">50</text>
        <text class="axis-label" x="470" y="677">20</text>
        <text class="axis-label" x="470" y="694">0</text>
        <text class="axis-label" x="470" y="777">20,000</text>
        <text class="axis-label" x="470" y="810">10,000</text>
        <rect x="70" y="851" width="388" height="21" fill="var(--timebar)"/>
        <text class="time-label" x="118" y="866">8am</text>
        <text class="time-label" x="217" y="866">9am</text>
        <text class="time-label" x="317" y="866">10am</text>
        <text class="time-label" x="416" y="866">11am</text>
      </g>

      <!-- shared price candles -->
      <g id="candles">
        <line class="wick" x1="76" y1="318" x2="76" y2="325"/><rect class="candle-up" x="73.5" y="319" width="5" height="5"/>
        <line class="wick" x1="83" y1="321" x2="83" y2="336"/><rect class="candle-down" x="80.5" y="322" width="5" height="11"/>
        <line class="wick" x1="90" y1="336" x2="90" y2="340"/><line class="doji" x1="87" y1="338" x2="93" y2="338"/>
        <line class="doji" x1="94" y1="338" x2="100" y2="338"/>
        <line class="wick" x1="104" y1="335" x2="104" y2="339"/><line class="doji" x1="101" y1="337" x2="107" y2="337"/>
        <line class="wick" x1="111" y1="331" x2="111" y2="339"/><rect class="candle-up" x="108.5" y="333" width="5" height="4"/>
        <line class="wick" x1="118" y1="333" x2="118" y2="338"/><line class="doji" x1="115" y1="335" x2="121" y2="335"/>
        <line class="wick" x1="124" y1="331" x2="124" y2="340"/><rect class="candle-down" x="121.5" y="333" width="5" height="5"/>
        <line class="doji" x1="128" y1="338" x2="134" y2="338"/>
        <line class="wick" x1="139" y1="336" x2="139" y2="342"/><line class="doji" x1="136" y1="339" x2="142" y2="339"/>
        <line class="wick" x1="148" y1="348" x2="148" y2="361"/><rect class="candle-down" x="145.5" y="350" width="5" height="8"/>
        <line class="wick" x1="157" y1="368" x2="157" y2="398"/><rect class="candle-down" x="154.5" y="370" width="5" height="25"/>
        <line class="wick" x1="166" y1="409" x2="166" y2="422"/><rect class="candle-down" x="163.5" y="412" width="5" height="7"/>
        <line class="wick" x1="174" y1="433" x2="174" y2="486"/><rect class="candle-down" x="171.5" y="439" width="5" height="26"/>
        <line class="wick" x1="183" y1="464" x2="183" y2="496"/><rect class="candle-down" x="180.5" y="470" width="5" height="15"/>
        <line class="wick" x1="191" y1="470" x2="191" y2="512"/><line class="doji" x1="188" y1="478" x2="194" y2="478"/>
        <line class="wick" x1="200" y1="462" x2="200" y2="488"/><rect class="candle-up" x="197.5" y="465" width="5" height="20"/>
        <line class="wick" x1="208" y1="456" x2="208" y2="466"/><rect class="candle-up" x="205.5" y="458" width="5" height="6"/>
        <line class="wick" x1="216" y1="455" x2="216" y2="465"/><rect class="candle-up" x="213.5" y="458" width="5" height="4"/>
        <line class="wick" x1="225" y1="449" x2="225" y2="463"/><rect class="candle-up" x="222.5" y="452" width="5" height="8"/>
        <line class="wick" x1="233" y1="445" x2="233" y2="460"/><rect class="candle-up" x="230.5" y="447" width="5" height="11"/>
        <line class="wick" x1="241" y1="437" x2="241" y2="447"/><rect class="candle-up" x="238.5" y="440" width="5" height="5"/>
        <line class="wick" x1="249" y1="428" x2="249" y2="442"/><rect class="candle-down" x="246.5" y="430" width="5" height="10"/>
        <line class="wick" x1="258" y1="435" x2="258" y2="442"/><line class="doji" x1="255" y1="438" x2="261" y2="438"/>
        <line class="wick" x1="266" y1="432" x2="266" y2="443"/><rect class="candle-up" x="263.5" y="435" width="5" height="5"/>
        <line class="wick" x1="274" y1="425" x2="274" y2="440"/><rect class="candle-up" x="271.5" y="428" width="5" height="10"/>
        <line class="wick" x1="282" y1="426" x2="282" y2="433"/><line class="doji" x1="279" y1="430" x2="285" y2="430"/>
        <line class="wick" x1="290" y1="402" x2="290" y2="433"/><rect class="candle-up" x="287.5" y="405" width="5" height="25"/>
        <line class="wick" x1="299" y1="382" x2="299" y2="400"/><rect class="candle-up" x="296.5" y="385" width="5" height="13"/>
        <line class="wick" x1="308" y1="386" x2="308" y2="397"/><rect class="candle-down" x="305.5" y="388" width="5" height="7"/>
        <line class="wick" x1="316" y1="388" x2="316" y2="407"/><rect class="candle-down" x="313.5" y="390" width="5" height="15"/>
        <line class="wick" x1="325" y1="398" x2="325" y2="423"/><rect class="candle-down" x="322.5" y="400" width="5" height="20"/>
        <line class="wick" x1="333" y1="400" x2="333" y2="412"/><line class="doji" x1="330" y1="405" x2="336" y2="405"/>
        <line class="wick" x1="341" y1="399" x2="341" y2="410"/><line class="doji" x1="338" y1="405" x2="344" y2="405"/>
        <line class="wick" x1="349" y1="398" x2="349" y2="410"/><line class="doji" x1="346" y1="403" x2="352" y2="403"/>
        <line class="wick" x1="357" y1="392" x2="357" y2="408"/><rect class="candle-up" x="354.5" y="395" width="5" height="10"/>
        <line class="wick" x1="366" y1="382" x2="366" y2="401"/><rect class="candle-up" x="363.5" y="385" width="5" height="13"/>
        <line class="wick" x1="373" y1="360" x2="373" y2="377"/><rect class="candle-up" x="370.5" y="362" width="5" height="13"/>
        <line class="wick" x1="382" y1="360" x2="382" y2="374"/><rect class="candle-down" x="379.5" y="362" width="5" height="10"/>
        <line class="wick" x1="390" y1="368" x2="390" y2="377"/><rect class="candle-down" x="387.5" y="370" width="5" height="5"/>
        <line class="wick" x1="398" y1="343" x2="398" y2="352"/><line class="doji" x1="395" y1="348" x2="401" y2="348"/>
        <line class="wick" x1="406" y1="333" x2="406" y2="352"/><rect class="candle-up" x="403.5" y="335" width="5" height="13"/>
        <line class="wick" x1="415" y1="319" x2="415" y2="334"/><rect class="candle-up" x="412.5" y="322" width="5" height="10"/>
        <line class="wick" x1="424" y1="318" x2="424" y2="327"/><line class="doji" x1="421" y1="322" x2="427" y2="322"/>
      </g>

      <!-- shared volume bars -->
      <g id="volume" class="vol-bar">
        <rect x="75" y="833" width="2" height="4"/><rect x="83" y="830" width="2" height="7"/>
        <rect x="91" y="832" width="2" height="5"/><rect x="99" y="832" width="2" height="5"/>
        <rect x="107" y="834" width="2" height="3"/><rect x="123" y="830" width="2" height="7"/>
        <rect x="131" y="830" width="2" height="7"/><rect x="139" y="830" width="2" height="7"/>
        <rect x="147" y="817" width="2" height="20"/><rect x="155" y="814" width="2" height="23"/>
        <rect x="163" y="820" width="2" height="17"/><rect x="171" y="768" width="2" height="69"/>
        <rect x="179" y="801" width="2" height="36"/><rect x="187" y="778" width="2" height="59"/>
        <rect x="195" y="811" width="2" height="26"/><rect x="203" y="811" width="2" height="26"/>
        <rect x="211" y="824" width="2" height="13"/><rect x="219" y="827" width="2" height="10"/>
        <rect x="227" y="817" width="2" height="20"/><rect x="235" y="820" width="2" height="17"/>
        <rect x="243" y="830" width="2" height="7"/><rect x="251" y="834" width="2" height="3"/>
        <rect x="259" y="827" width="2" height="10"/><rect x="267" y="827" width="2" height="10"/>
        <rect x="275" y="834" width="2" height="3"/><rect x="283" y="824" width="2" height="13"/>
        <rect x="291" y="797" width="2" height="40"/><rect x="299" y="817" width="2" height="20"/>
        <rect x="307" y="820" width="2" height="17"/><rect x="315" y="830" width="2" height="7"/>
        <rect x="323" y="814" width="2" height="23"/><rect x="331" y="830" width="2" height="7"/>
        <rect x="339" y="827" width="2" height="10"/><rect x="347" y="827" width="2" height="10"/>
        <rect x="355" y="824" width="2" height="13"/><rect x="363" y="820" width="2" height="17"/>
        <rect x="371" y="832" width="2" height="5"/><rect x="379" y="824" width="2" height="13"/>
        <rect x="387" y="827" width="2" height="10"/><rect x="395" y="817" width="2" height="20"/>
        <rect x="403" y="820" width="2" height="17"/><rect x="411" y="817" width="2" height="20"/>
        <rect x="419" y="834" width="2" height="3"/>
      </g>
    </defs>

    <!-- divider rules -->
    <line x1="70" y1="200" x2="1130" y2="200" stroke="var(--ink)" stroke-width="1.2"/>
    <line x1="599" y1="152" x2="599" y2="873" stroke="var(--ink)" stroke-width="1.2"/>

    <!-- entry side -->
    <g class="chart chart--entry">
      <use href="#frame"/>
      <use href="#candles"/>
      <use href="#volume"/>
      <polyline fill="none" stroke="var(--rsi-glow)" stroke-width="3" stroke-linejoin="round"
        points="70,663 82,683 98,683 110,665 120,665 130,677 140,677 150,686 165,687 188,689 204,659 214,659 220,651 228,651 236,633 242,633 248,649 258,649 266,622 274,622 290,607 298,605 312,632 324,656 336,635 346,643 354,643 372,610 386,634 396,627 402,627 416,612 424,611"/>
      <polyline fill="none" stroke="var(--rsi-core)" stroke-width="1" stroke-linejoin="round"
        points="70,663 82,683 98,683 110,665 120,665 130,677 140,677 150,686 165,687 188,689 204,659 214,659 220,651 228,651 236,633 242,633 248,649 258,649 266,622 274,622 290,607 298,605 312,632 324,656 336,635 346,643 354,643 372,610 386,634 396,627 402,627 416,612 424,611"/>
      <path d="M409 262 h14 v22 h9 l-16 24 l-16 -24 h9 z" fill="#ffffff" stroke="#111111" stroke-width="2" stroke-linejoin="round"/>
    </g>

    <!-- exit side -->
    <g class="chart chart--exit" transform="translate(563 0)">
      <use href="#frame"/>
      <use href="#candles"/>
      <use href="#volume"/>
      <line class="wick" x1="432" y1="316" x2="432" y2="324"/><rect class="candle-up" x="429.5" y="318" width="5" height="4"/>
      <line class="wick" x1="439" y1="314" x2="439" y2="321"/><line class="doji" x1="436" y1="318" x2="442" y2="318"/>
      <line class="wick" x1="446" y1="315" x2="446" y2="322"/><line class="doji" x1="443" y1="318" x2="449" y2="318"/>
      <line class="doji" x1="443" y1="322" x2="449" y2="322" transform="translate(6 0)"/>
      <g class="vol-bar">
        <rect x="427" y="817" width="2" height="20"/><rect x="435" y="824" width="2" height="13"/>
        <rect x="442" y="827" width="2" height="10"/><rect x="449" y="834" width="2" height="3"/>
      </g>
      <polyline fill="none" stroke="var(--rsi-glow)" stroke-width="5" stroke-linejoin="round"
        points="70,663 82,683 98,683 110,665 120,665 130,677 140,677 150,686 165,687 188,689 204,659 214,659 220,651 228,651 236,633 242,633 248,649 258,649 266,622 274,622 290,607 298,605 312,632 324,656 336,635 346,643 354,643 372,610 386,634 396,627 402,627 416,612 424,611 438,607 451,622"/>
      <polyline fill="none" stroke="var(--rsi-core)" stroke-width="1.5" stroke-linejoin="round"
        points="70,663 82,683 98,683 110,665 120,665 130,677 140,677 150,686 165,687 188,689 204,659 214,659 220,651 228,651 236,633 242,633 248,649 258,649 266,622 274,622 290,607 298,605 312,632 324,656 336,635 346,643 354,643 372,610 386,634 396,627 402,627 416,612 424,611 438,607 451,622"/>
      <path d="M409 262 h14 v22 h9 l-16 24 l-16 -24 h9 z" fill="#ffffff" stroke="#111111" stroke-width="2" stroke-linejoin="round"/>
    </g>
  </svg>
</div>
</body>
</html>
```